Photo-Video Combo Package Flyer

Need to create a flyer to showcase a combo package featuring photography and videography from two separate companies. I need an 8 1/2 X 11 flyer in .psd so I can make changes as needed as well as all fonts
Target Market(s)
Brides & Grooms
Industry/Entity Type
Wedding Photography
Requirements
Must have
- see word doc
Nice to have
- please visit websites for inspiration
- https://quietharborimages.com/
- www.kqbrt.com

```html
<!DOCTYPE html>
<html lang="en">
<head>
<meta charset="utf-8">
<title>Photo Video Combo Flyer</title>
<link href="https://fonts.googleapis.com/css2?family=Open+Sans:ital,wght@0,400;0,600;0,700;1,400;1,600&family=Playfair+Display:ital@1&family=Baloo+2:wght@500&display=swap" rel="stylesheet">
<style>
  :root {
    --page-bg: #e4e4e0;
    --paper: #ffffff;
    --header-bg: #f6f4f3;
    --salmon: #dd9d86;
    --copper: #a9553f;
    --deep-red: #8b3324;
    --stamp-red: #c8242a;
    --ink: #2a2a2a;
    --muted: #444;
    --photo-sunset: linear-gradient(160deg, #f0b070 0%, #b0787a 45%, #3d4b63 100%);
    --photo-sea: linear-gradient(180deg, #e7a66a 0%, #d98c58 40%, #375a7a 100%);
    --photo-harbor: linear-gradient(180deg, #c9a287 0%, #6d6370 50%, #2d3441 100%);
    --photo-bride: linear-gradient(160deg, #efe9e4 0%, #d9cfc8 50%, #a7b39a 100%);
  }
  * { box-sizing: border-box; margin: 0; padding: 0; }
  html, body { width: 1200px; height: 804px; overflow: hidden; background: var(--page-bg); }
  .flyer {
    position: absolute; left: 297px; top: 10px; width: 606px; height: 784px;
    background: var(--paper); font-family: "Open Sans", sans-serif; color: var(--ink);
    overflow: hidden;
  }
  .abs { position: absolute; }
  .masthead { left: 0; top: 0; width: 606px; height: 88px; background: var(--header-bg); }
  .brand {
    font-family: "Open Sans", sans-serif; font-weight: 600; font-size: 19px;
    color: var(--copper); display: flex; align-items: center; gap: 8px;
  }
  .brand-photo { left: 28px; top: 30px; }
  .brand-video { right: 24px; top: 30px; color: var(--deep-red); }
  .brand-dot { width: 12px; height: 12px; border-radius: 50%; background: currentColor; }
  .photo { display: block; }
  .photo-deck { left: 0; top: 88px; width: 229px; height: 136px; background: var(--photo-sunset); }
  .photo-sea { left: 0; top: 227px; width: 192px; height: 141px; background: var(--photo-sea); }
  .photo-harbor { left: 196px; top: 227px; width: 185px; height: 141px; background: var(--photo-harbor); }
  .photo-bride { left: 388px; top: 88px; width: 218px; height: 280px; background: var(--photo-bride); }
  .combo-box {
    left: 233px; top: 88px; width: 148px; height: 136px; background: var(--salmon);
    color: #fff; font-family: "Playfair Display", serif; font-style: italic; text-align: center;
    padding-top: 14px; line-height: 1.05;
  }
  .combo-title { font-size: 19px; }
  .combo-price { font-size: 34px; margin-top: 2px; }
  .combo-save { font-size: 19px; }
  .save-stamp {
    left: 160px; top: 196px; width: 92px; height: 92px; border-radius: 50%;
    background: var(--stamp-red);
  }
  .intro {
    left: 28px; top: 380px; width: 554px; font-size: 8px; font-style: italic;
    line-height: 1.45; color: var(--muted);
  }
  .section-head { display: flex; align-items: center; top: 436px; }
  .section-head .icon {
    width: 44px; height: 44px; border-radius: 50%; background: var(--salmon);
    display: flex; align-items: center; justify-content: center; position: relative; z-index: 2;
  }
  .section-head .label {
    background: linear-gradient(90deg, #f7e6df, #fbf2ee); border-radius: 0 14px 14px 0;
    font-style: italic; font-weight: 600; font-size: 14.5px; color: #333;
    padding: 3px 12px 4px 14px; margin-left: -4px;
  }
  .head-photo { left: 26px; }
  .head-video { left: 315px; }
  .package {
    top: 475px; width: 280px; height: 181px; border: 3px solid var(--copper);
    border-radius: 20px; padding: 10px 10px 0 10px;
  }
  .package-photo { left: 15px; }
  .package-video { left: 311px; }
  .features { display: grid; grid-template-columns: 1fr 1fr; column-gap: 8px; row-gap: 6px; list-style: none; height: 86px; }
  .features li {
    display: flex; gap: 4px; font-size: 8.3px; font-style: italic; line-height: 1.3; color: #222;
  }
  .features li svg { flex: none; margin-top: 1px; }
  .retail {
    font-family: "Baloo 2", sans-serif; font-weight: 500; color: var(--deep-red);
    font-size: 16.5px; text-align: center; display: flex; justify-content: center; align-items: center; gap: 6px;
  }
  .provided { text-align: center; font-size: 9.5px; color: #333; margin-top: 1px; }
  .provider {
    font-family: "Baloo 2", sans-serif; font-weight: 500; color: var(--deep-red);
    font-size: 18px; text-align: center; line-height: 1.3;
  }
  .contact { top: 670px; text-align: center; }
  .contact-photo { left: 55px; width: 220px; }
  .contact-video { left: 352px; width: 210px; }
  .contact h3 { font-size: 15px; font-weight: 700; color: var(--deep-red); line-height: 1.2; }
  .contact .phone { font-size: 16.5px; font-weight: 700; color: #111; display: flex; justify-content: center; align-items: center; gap: 5px; line-height: 1.15; }
  .contact .web { font-size: 11px; color: #222; display: flex; justify-content: center; align-items: center; gap: 6px; margin-top: 2px; }
  .upgrade { left: 248px; top: 693px; width: 110px; text-align: center; font-size: 12px; font-weight: 600; line-height: 1.25; color: #222; }
  .foot-band { left: 18px; top: 733px; width: 572px; height: 29px; background: #c9826d; opacity: .85; }
</style>
</head>
<body>
<main class="flyer">
  <header class="abs masthead"></header>
  <div class="abs brand brand-photo">Quiet Harbor Images</div>
  <div class="abs brand brand-video"><span class="brand-dot"></span>Kestrel Bright Video</div>

  <div class="abs photo photo-deck" role="img" aria-label="Couple embracing on a ship deck at sunset"></div>
  <div class="abs combo-box">
    <div class="combo-title">Photo Video<br>Combo Price</div>
    <div class="combo-price">$2999</div>
    <div class="combo-save">($750 Savings)</div>
  </div>
  <div class="abs photo photo-sea" role="img" aria-label="Couple kissing by the sea at sunset"></div>
  <div class="abs photo photo-harbor" role="img" aria-label="Couple on a marina dock at dusk"></div>
  <div class="abs photo photo-bride" role="img" aria-label="Bride holding a white bouquet"></div>

  <div class="abs save-stamp" role="img" aria-label="Savings badge"></div>

  <p class="abs intro">The Photo-Video combo package is the best way to hire your Photographer and videographer. Both companies are highly rated by The Vow List and Aisle Guide as well as recommended by the area's top wedding venues. When your photographer and videographer are working together your wedding day will run smoothly, so you can just enjoy yourself and have fun! Contact us to learn more and schedule a consultation.</p>

  <div class="abs section-head head-photo">
    <div class="icon"><svg width="24" height="20" viewBox="0 0 24 20" fill="none" stroke="#fff" stroke-width="1.6"><rect x="1.5" y="5" width="21" height="13" rx="2"/><path d="M8 5 L9.5 2 H14.5 L16 5"/><circle cx="12" cy="11.5" r="4"/></svg></div>
    <div class="label">Photo Package Includes</div>
  </div>
  <div class="abs section-head head-video">
    <div class="icon"><svg width="24" height="22" viewBox="0 0 24 22" fill="none" stroke="#fff" stroke-width="1.6"><circle cx="7" cy="5" r="3.5"/><circle cx="14" cy="5" r="3.5"/><rect x="2" y="10" width="14" height="9" rx="1.5"/><path d="M16 13 L22 10 V19 L16 16"/></svg></div>
    <div class="label">Video Package Includes</div>
  </div>

  <section class="abs package package-photo">
    <ul class="features">
      <li><svg width="8" height="8" viewBox="0 0 8 8"><circle cx="4" cy="4" r="3.4" fill="none" stroke="#333" stroke-width=".8"/><path d="M2.4 4 L3.6 5.1 L5.6 2.9" fill="none" stroke="#333" stroke-width=".8"/></svg>1 Hr Engagement Shoot</li>
      <li><svg width="8" height="8" viewBox="0 0 8 8"><circle cx="4" cy="4" r="3.4" fill="none" stroke="#333" stroke-width=".8"/><path d="M2.4 4 L3.6 5.1 L5.6 2.9" fill="none" stroke="#333" stroke-width=".8"/></svg>Images professionally edited in house</li>
      <li><svg width="8" height="8" viewBox="0 0 8 8"><circle cx="4" cy="4" r="3.4" fill="none" stroke="#333" stroke-width=".8"/><path d="M2.4 4 L3.6 5.1 L5.6 2.9" fill="none" stroke="#333" stroke-width=".8"/></svg>One photographer up to 7 hours on location for wedding</li>
      <li><svg width="8" height="8" viewBox="0 0 8 8"><circle cx="4" cy="4" r="3.4" fill="none" stroke="#333" stroke-width=".8"/><path d="M2.4 4 L3.6 5.1 L5.6 2.9" fill="none" stroke="#333" stroke-width=".8"/></svg>Beautiful online gallery to download from</li>
      <li><svg width="8" height="8" viewBox="0 0 8 8"><circle cx="4" cy="4" r="3.4" fill="none" stroke="#333" stroke-width=".8"/><path d="M2.4 4 L3.6 5.1 L5.6 2.9" fill="none" stroke="#333" stroke-width=".8"/></svg>High Resolution, Edited digital images</li>
      <li><svg width="8" height="8" viewBox="0 0 8 8"><circle cx="4" cy="4" r="3.4" fill="none" stroke="#333" stroke-width=".8"/><path d="M2.4 4 L3.6 5.1 L5.6 2.9" fill="none" stroke="#333" stroke-width=".8"/></svg>Print release to print at the lab of your choice</li>
    </ul>
    <div class="retail"><svg width="14" height="14" viewBox="0 0 14 14"><circle cx="7" cy="7" r="5.8" fill="none" stroke="#8b3324" stroke-width="1.4"/><path d="M4.2 7 L6.2 9 L9.8 5.2" fill="none" stroke="#8b3324" stroke-width="1.4"/></svg>Normal Retail Price $2450</div>
    <div class="provided">Photography provided by</div>
    <div class="provider">Quiet Harbor Images</div>
  </section>

  <section class="abs package package-video">
    <ul class="features">
      <li><svg width="8" height="8" viewBox="0 0 8 8"><circle cx="4" cy="4" r="3.4" fill="none" stroke="#333" stroke-width=".8"/><path d="M2.4 4 L3.6 5.1 L5.6 2.9" fill="none" stroke="#333" stroke-width=".8"/></svg>Up To 6 Hours of Coverage</li>
      <li><svg width="8" height="8" viewBox="0 0 8 8"><circle cx="4" cy="4" r="3.4" fill="none" stroke="#333" stroke-width=".8"/><path d="M2.4 4 L3.6 5.1 L5.6 2.9" fill="none" stroke="#333" stroke-width=".8"/></svg>A Cinematic highlight Recap 3-4 minutes</li>
      <li><svg width="8" height="8" viewBox="0 0 8 8"><circle cx="4" cy="4" r="3.4" fill="none" stroke="#333" stroke-width=".8"/><path d="M2.4 4 L3.6 5.1 L5.6 2.9" fill="none" stroke="#333" stroke-width=".8"/></svg>Documentary Style Video Edit 60-90 Minutes</li>
      <li><svg width="8" height="8" viewBox="0 0 8 8"><circle cx="4" cy="4" r="3.4" fill="none" stroke="#333" stroke-width=".8"/><path d="M2.4 4 L3.6 5.1 L5.6 2.9" fill="none" stroke="#333" stroke-width=".8"/></svg>3 Personalized DVDs</li>
      <li><svg width="8" height="8" viewBox="0 0 8 8"><circle cx="4" cy="4" r="3.4" fill="none" stroke="#333" stroke-width=".8"/><path d="M2.4 4 L3.6 5.1 L5.6 2.9" fill="none" stroke="#333" stroke-width=".8"/></svg>Edited Background Music</li>
    </ul>
    <div class="retail"><svg width="14" height="14" viewBox="0 0 14 14"><circle cx="7" cy="7" r="5.8" fill="none" stroke="#8b3324" stroke-width="1.4"/><path d="M4.2 7 L6.2 9 L9.8 5.2" fill="none" stroke="#8b3324" stroke-width="1.4"/></svg>Normal Retail Price $1299</div>
    <div class="provided">Videography provided by</div>
    <div class="provider">Kestrel Bright Video</div>
  </section>

  <div class="abs contact contact-photo">
    <h3>Photo Contact Info</h3>
    <div class="phone"><svg width="12" height="12" viewBox="0 0 12 12"><circle cx="6" cy="6" r="6" fill="#111"/><path d="M4 3 L5 5 L4.5 5.6 Q5.3 7 6.5 7.6 L7 7 L9 8 L8.4 9.2 Q5.5 9.2 3 5.2 Z" fill="#fff"/></svg>941-555-0172</div>
    <div class="web"><svg width="11" height="11" viewBox="0 0 11 11" fill="none" stroke="#222" stroke-width=".9"><circle cx="5.5" cy="5.5" r="4.8"/><ellipse cx="5.5" cy="5.5" rx="2.2" ry="4.8"/><path d="M0.7 5.5 H10.3"/></svg>quietharborimages.com</div>
  </div>
  <div class="abs upgrade">Plus Save 10% off any upgrades</div>
  <div class="abs contact contact-video">
    <h3>Video Contact Info</h3>
    <div class="phone"><svg width="12" height="12" viewBox="0 0 12 12"><circle cx="6" cy="6" r="6" fill="#111"/><path d="M4 3 L5 5 L4.5 5.6 Q5.3 7 6.5 7.6 L7 7 L9 8 L8.4 9.2 Q5.5 9.2 3 5.2 Z" fill="#fff"/></svg>941-555-0139</div>
    <div class="web"><svg width="11" height="11" viewBox="0 0 11 11" fill="none" stroke="#222" stroke-width=".9"><circle cx="5.5" cy="5.5" r="4.8"/><ellipse cx="5.5" cy="5.5" rx="2.2" ry="4.8"/><path d="M0.7 5.5 H10.3"/></svg>www.kqbrt.com</div>
  </div>

  <div class="abs foot-band" role="img" aria-label="Decorative striped copper band"></div>
</main>
</body>
</html>
```